Velmora health leaflet

We are looking for a new brand identity for our clinic to start with a new leaflet for communication. For current brand identity please look at our website Www.velmorahealth.cz. We would like to use less of the blue but more of the green turquoise and white. The logo should remain. See attached. We received few ideas but not sure about them. The design should be elegant and simple. Premium
#729694 Hex Color Code
The hexadecimal color code #729694 is a shade of cyan. In the RGB color model #729694 is composed of 44.71% red, 58.82% green and 58.04% blue. In the HSL color space #729694 has a hue of 177° (degrees), 15% saturation and 52% lightness. This color has an approximate wavelength of 492.66 nm.
Main headlines
Playfair Display
Serif, elegant
Body & UI
Lato
Clean, modern
Look and feel
Each slider illustrates characteristics of the customer's brand and the style your logo design should communicate.

```html
<!DOCTYPE html>
<html lang="en">
<head>
<meta charset="utf-8">
<title>Velmora health leaflet</title>
<link rel="stylesheet" href="https://fonts.googleapis.com/css2?family=Merriweather:wght@300;400&family=Lato:wght@400;700&display=swap">
<style>
  :root {
    --teal: #4b8c8a;
    --teal-dark: #3f7f7d;
    --white: #ffffff;
    --ink: #2b2f30;
    --muted: #6f7677;
    --rule: #7fb3b0;
    --page: #ffffff;
  }
  * { margin: 0; padding: 0; box-sizing: border-box; }
  html, body { width: 1200px; height: 1000px; overflow: hidden; background: var(--page); }
  body { position: relative; font-family: "Lato", Arial, sans-serif; color: var(--ink); }

  .sheet-rule {
    position: absolute; left: 55px; top: 250px; width: 955px; height: 0;
    border-top: 2px dotted var(--rule);
  }

  .panel {
    position: absolute; top: 355px; height: 438px; overflow: hidden;
    box-shadow: 0 2px 6px rgba(0,0,0,0.12);
  }
  .panel--cover { left: 54px; width: 219px; background: var(--teal); color: var(--white); }
  .panel--portrait { left: 297px; width: 216px; background: var(--white); border: 1px solid #e2e4e4; }
  .panel--services { left: 535px; width: 220px; background: var(--teal); color: var(--white); }
  .panel--contact { left: 779px; width: 229px; background: var(--white); border: 1px solid #e2e4e4; }

  .wordmark {
    position: absolute; left: 0; right: 0; bottom: 20px; text-align: center;
    font-family: "Lato", Arial, sans-serif; font-size: 7.5px; font-weight: 400;
    letter-spacing: 0.8px; text-transform: uppercase;
  }
  .panel--cover .wordmark, .panel--services .wordmark { color: var(--white); }
  .panel--portrait .wordmark { color: var(--ink); }

  /* Cover */
  .cover__headline {
    position: absolute; right: 14px; top: 30px; width: 200px; text-align: right;
    font-family: "Merriweather", Georgia, serif; font-weight: 300;
    font-size: 29px; line-height: 36px;
  }
  .cover__rule { position: absolute; left: 21px; top: 230px; width: 1px; height: 208px; background: rgba(255,255,255,0.55); }
  .cover__side-text {
    position: absolute; left: 20px; top: 250px; font-size: 5.5px; letter-spacing: 0.6px;
    color: rgba(255,255,255,0.8); transform-origin: left top; transform: rotate(90deg);
    white-space: nowrap; background: var(--teal); padding: 0 4px; line-height: 7px;
  }
  .cover__tagline {
    position: absolute; left: 56px; top: 262px; width: 150px;
    font-size: 10.5px; line-height: 13px;
  }

  /* Portrait */
  .portrait__image {
    position: absolute; left: 0; top: 0; width: 216px; height: 438px;
    background: linear-gradient(90deg, #9a9c9d 0%, #cfd1d2 22%, #ecedee 42%, #fafafa 62%, #ffffff 100%);
  }
  .portrait__rule { position: absolute; left: 178px; top: 0; width: 1px; height: 438px; background: #e1e3e3; }

  /* Services */
  .services__intro, .services__item {
    position: absolute; left: 27px; width: 180px; font-size: 6.6px; line-height: 9px;
    color: rgba(255,255,255,0.9);
  }
  .services__pillars {
    position: absolute; left: 15px; top: 85px; width: 192px; height: 29px;
    border: 1px solid rgba(255,255,255,0.5); border-radius: 5px;
    font-size: 5.6px; letter-spacing: 0.6px; line-height: 9px; text-align: center;
    padding-top: 5px; color: rgba(255,255,255,0.92); text-transform: uppercase;
  }

  /* Contact */
  .contact__image {
    position: absolute; left: 0; top: 18px; width: 229px; height: 164px;
    background: linear-gradient(180deg, #6f97c7 0%, #a9c3dc 38%, #8fa2ad 62%, #56686b 100%);
  }
  .contact__name {
    position: absolute; left: 0; right: 0; top: 210px; text-align: center;
    font-family: "Merriweather", Georgia, serif; font-weight: 400; font-size: 22px; color: var(--ink);
  }
  .contact__intro {
    position: absolute; left: 26px; top: 278px; width: 178px;
    font-size: 5.8px; line-height: 8px; color: var(--muted);
  }
  .contact__block { position: absolute; font-size: 6.2px; line-height: 8.5px; color: var(--teal); }
  .contact__label { font-weight: 700; font-size: 6.5px; letter-spacing: 0.3px; text-transform: uppercase; }
  .contact__block--hours { left: 26px; top: 330px; }
  .contact__block--hours .contact__label { color: var(--teal-dark); }
  .contact__block--hours-alt { left: 116px; top: 338px; text-align: center; width: 80px; }
  .contact__block--address { top: 383px; width: 90px; text-align: center; }
  .contact__block--address .contact__label { color: var(--ink); }
  .contact__block--address-a { left: 18px; }
  .contact__block--address-b { left: 122px; }
</style>
</head>
<body>
  <div class="sheet-rule"></div>

  <section class="panel panel--cover">
    <h1 class="cover__headline">Add Healthy<br>Years to<br>Your to<br>Life</h1>
    <div class="cover__rule"></div>
    <div class="cover__side-text">Velmora health longevity</div>
    <p class="cover__tagline">Europe's first center of<br>excellence for medicine<br>&amp; healthy longevity.</p>
    <div class="wordmark">Velmora health</div>
  </section>

  <section class="panel panel--portrait">
    <div class="portrait__image" role="img" aria-label="Soft black and white profile portrait fading into white"></div>
    <div class="portrait__rule"></div>
    <div class="wordmark">Velmora health</div>
  </section>

  <section class="panel panel--services">
    <p class="services__intro" style="top:25px">Fast access to your personal doctor<br>Priority appointments across all key fields</p>
    <p class="services__intro" style="top:51px">30+ specialists across all key fields<br>24/7 availability wherever you are</p>
    <div class="services__pillars">Prevention · Treatment · Longevity · Innovation<br>Presence · Vision · Moment · Achievement</div>
    <p class="services__item" style="top:138px">Why a Velmora health membership<br>Plans tailored to your medical needs</p>
    <p class="services__item" style="top:165px">Direct contact with a dedicated medical concierge<br>available day and night for you</p>
    <p class="services__item" style="top:191px">Direct contact with your leading physician and team<br>coordinated across every specialist</p>
    <p class="services__item" style="top:218px">Direct access to the most current testing<br>personal plans for long term well being</p>
    <p class="services__item" style="top:245px">Personal guidance with clear long term care planning<br>tracked progress and yearly health reviews</p>
    <p class="services__item" style="top:276px">Home visits available in your region<br>and fully discreet personal care</p>
    <p class="services__item" style="top:319px">Two locations in Prague<br>and international partner clinics</p>
    <div class="wordmark">Www.velmorahealth.cz</div>
  </section>

  <section class="panel panel--contact">
    <div class="contact__image" role="img" aria-label="Modern glass office building under a blue sky"></div>
    <div class="contact__name">Velmora health</div>
    <p class="contact__intro">Velmora health brings private medicine and longevity care together under one roof, with personal physicians, advanced diagnostics and a calm setting designed around you and your family.</p>
    <div class="contact__block contact__block--hours">
      <div class="contact__label">Consultation hours</div>
      Mon – Fri: 8:00 - 19:00<br>care@velmorahealth.cz
    </div>
    <div class="contact__block contact__block--hours-alt">
      Prague clinic<br>Mo – Fr: 8:00 - 18:00
    </div>
    <div class="contact__block contact__block--address contact__block--address-a">
      <div class="contact__label">Velmora health</div>
      Lindova 1420<br>140 00 Praha 4
    </div>
    <div class="contact__block contact__block--address contact__block--address-b">
      <div class="contact__label">Velmora health</div>
      Korunni 58<br>120 00 Praha 2
    </div>
  </section>
</body>
</html>
```